Lawyers in the Netherlands website + logo

We are going in 2015 to launch a website where all law firms in the Netherlands and have the opportunity to place an ad program.

The domain name wil be:

kwelderhofpunt.website

We want a responsive PSD bootstrap twitter 1170 pixel grid.
for the homepage, result page and the detail page of the customer.

This sites we like:
https://www.vorqami.com/lawyers

https://lawyers.vorqami.com/lawyer/tad-mirske-5820734

http://solicitordirectory.brevmoor.co.uk/
Map of the Netherlands?

http://solicitordirectory.brevmoor.co.uk/listing/category-search/commercial
http://www.quellbarn.com.au/find-a-lawyer/banking-finance-law/

```html
<!DOCTYPE html>
<html lang="en">
<head>
<meta charset="utf-8">
<title>Kwelderhofpunt – Find Law Firms in the Netherlands</title>
<link href="https://fonts.googleapis.com/css2?family=Fjalla+One&family=Open+Sans:wght@400;600&display=swap" rel="stylesheet">
<style>
  :root {
    --navy: #0f2b5b;
    --navy-deep: #0c2450;
    --gold: #e3a01b;
    --gold-dark: #b57c0c;
    --ink: #1d2d4f;
    --text: #2b3a55;
    --panel: #f0f0f1;
    --white: #ffffff;
    --rule: #d6d6d6;
  }
  * { box-sizing: border-box; margin: 0; padding: 0; }
  html, body { width: 811px; height: 1200px; overflow: hidden; }
  body {
    position: relative;
    background: var(--white);
    font-family: "Open Sans", Arial, sans-serif;
    color: var(--text);
  }
  h1, h2 { font-weight: 400; }
  .top-rule { position: absolute; left: 0; top: 0; width: 811px; height: 3px; background: var(--rule); }

  /* Header */
  .site-header { position: absolute; left: 0; top: 3px; width: 811px; height: 78px; }
  .brand { position: absolute; left: 42px; top: 24px; display: flex; align-items: center; gap: 10px; }
  .brand-dot { width: 30px; height: 30px; border-radius: 50%; background: var(--navy); }
  .brand-name { font-weight: 600; font-size: 20px; letter-spacing: 1.5px; color: var(--navy); white-space: nowrap; }
  .header-btn {
    position: absolute; top: 25px; height: 19px; padding: 0 6px;
    background: var(--gold); border: 1px solid var(--gold-dark);
    box-shadow: 1px 2px 0 rgba(0,0,0,.25);
    font-size: 10.5px; line-height: 17px; color: var(--navy-deep);
    white-space: nowrap; text-align: center;
  }
  .btn-sign-in { left: 602px; }
  .btn-get-listed { left: 666px; width: 102px; padding: 0; }

  /* Navigation */
  .main-nav { position: absolute; left: 0; top: 81px; width: 811px; height: 37px; background: var(--navy); }
  .main-nav a {
    position: absolute; top: 0; height: 37px; line-height: 37px; white-space: nowrap;
    font-size: 10px; color: var(--white); text-decoration: none; text-transform: uppercase; letter-spacing: .2px;
  }
  .main-nav .is-active { left: 42px; width: 48px; background: var(--gold); text-align: center; color: var(--navy-deep); }
  .nav-gold { position: absolute; left: 0; top: 118px; width: 811px; height: 3px; background: var(--gold); }

  /* Hero */
  .hero-photo {
    position: absolute; left: 0; top: 121px; width: 811px; height: 273px;
    background: linear-gradient(180deg, #d9dde2 0%, #b9bec6 45%, #8c8f95 70%, #cfd2d6 100%);
  }
  .hero-band { position: absolute; left: 0; top: 394px; width: 811px; height: 6px; background: #c9cbce; }
  .search-panel {
    position: absolute; left: 157px; top: 217px; width: 499px; height: 117px;
    background: rgba(40,48,62,.55); border: 1px solid rgba(255,255,255,.55);
  }
  .search-title {
    position: absolute; left: 0; top: 12px; width: 100%; text-align: center; white-space: nowrap;
    font-family: "Fjalla One", Arial, sans-serif; font-size: 21px; color: var(--white);
  }
  .search-field {
    position: absolute; top: 51px; height: 35px; background: var(--white); white-space: nowrap;
    font-size: 13px; line-height: 35px; padding-left: 11px; color: #4a4f5a;
  }
  .field-issue { left: 26px; width: 224px; }
  .field-city { left: 252px; width: 184px; }
  .search-btn { position: absolute; left: 436px; top: 51px; width: 35px; height: 35px; background: var(--gold); }

  /* Location section */
  .location-bg { position: absolute; left: 0; top: 400px; width: 811px; height: 120px; background: linear-gradient(180deg, #eef0f4, #ffffff); }
  .eyebrow { position: absolute; left: 40px; top: 421px; font-family: "Fjalla One", Arial, sans-serif; font-size: 17px; color: var(--ink); }
  .section-title { position: absolute; left: 40px; top: 441px; font-family: "Fjalla One", Arial, sans-serif; font-size: 31px; color: var(--ink); white-space: nowrap; }
  .section-lead { position: absolute; left: 40px; top: 488px; font-size: 18px; color: var(--ink); white-space: nowrap; }

  .city-list { position: absolute; top: 562px; list-style: none; }
  .city-list li { position: relative; height: 18.6px; padding-left: 11px; font-size: 10px; line-height: 18.6px; color: var(--navy); white-space: nowrap; }
  .city-list li::before {
    content: ""; position: absolute; left: 0; top: 6px; width: 4px; height: 4px;
    border-right: 2px solid var(--gold); border-bottom: 2px solid var(--gold); transform: rotate(-45deg);
  }
  .col-1 { left: 42px; } .col-2 { left: 150px; } .col-3 { left: 252px; } .col-4 { left: 346px; }

  .region-map {
    position: absolute; left: 502px; top: 514px; width: 265px; height: 306px;
    background: radial-gradient(ellipse at 55% 45%, #cfcfcf 0%, #c4c4c4 60%, #d8d8d8 100%);
    border-radius: 40% 30% 35% 45%;
  }
  .map-tag {
    position: absolute; left: 667px; top: 557px; width: 58px; height: 20px;
    background: var(--white); border: 1px solid #777; font-size: 11px; line-height: 18px; text-align: center; color: #222;
  }

  /* Info section */
  .info-panel { position: absolute; left: 0; top: 860px; width: 811px; height: 274px; background: var(--panel); }
  .info-wedge { position: absolute; left: 0; top: 720px; }
  .info-title { position: absolute; left: 40px; top: 890px; font-family: "Fjalla One", Arial, sans-serif; font-size: 31px; color: var(--ink); white-space: nowrap; }
  .info-lead { position: absolute; left: 40px; top: 934px; font-size: 17px; color: var(--ink); white-space: nowrap; }
  .feature { position: absolute; top: 985px; width: 240px; text-align: center; }
  .feature svg { display: block; margin: 0 auto; }
  .feature-label { margin-top: 20px; font-family: "Fjalla One", Arial, sans-serif; font-size: 17px; color: var(--ink); white-space: nowrap; }
  .feat-qa { left: 40px; } .feat-centers { left: 284px; } .feat-codes { left: 529px; }

  /* Footer */
  .footer-gold { position: absolute; left: 0; top: 1134px; width: 811px; height: 3px; background: var(--gold); }
  .site-footer { position: absolute; left: 0; top: 1137px; width: 811px; height: 63px; background: var(--navy); }
  .footer-links { position: absolute; left: 42px; top: 25px; font-size: 10.5px; color: #b8c3d8; white-space: nowrap; }
  .footer-links span { margin: 0 9px; }
  .copyright { position: absolute; right: 42px; top: 28px; font-size: 8px; color: #b8c3d8; white-space: nowrap; }
</style>
</head>
<body>
  <div class="top-rule"></div>

  <header class="site-header">
    <div class="brand"><span class="brand-dot"></span><span class="brand-name">KWELDERHOFPUNT</span></div>
    <div class="header-btn btn-sign-in">Sign In</div>
    <div class="header-btn btn-get-listed">Lawyers Get Listed</div>
  </header>

  <nav class="main-nav">
    <a class="is-active">Home</a>
    <a style="left:114px">Find a Lawyer</a>
    <a style="left:218px">Lawyer Marketing</a>
    <a style="left:348px">Legal Answers</a>
    <a style="left:457px">More ▾</a>
  </nav>
  <div class="nav-gold"></div>

  <div class="hero-photo" role="img" aria-label="Photo of a team of lawyers meeting around a conference table in a bright office"></div>
  <div class="hero-band"></div>
  <div class="search-panel">
    <div class="search-title">Let us help you find a Law Firms around the Netherlands</div>
    <div class="search-field field-issue">Search Legal Issue or Law Firms</div>
    <div class="search-field field-city">City Here</div>
    <div class="search-btn">
      <svg width="35" height="35" viewBox="0 0 35 35"><circle cx="16" cy="15.5" r="6.5" fill="none" stroke="#fff" stroke-width="3"/><line x1="20.5" y1="20" x2="26" y2="25.5" stroke="#fff" stroke-width="4" stroke-linecap="round"/></svg>
    </div>
  </div>

  <div class="location-bg"></div>
  <div class="eyebrow">Find Law Firms in</div>
  <h1 class="section-title">Netherlands by Location</h1>
  <p class="section-lead">Either choose your location from the list of citys or use the map</p>

  <ul class="city-list col-1"><li>Almere</li><li>Amersfoort</li><li>Amsterdam</li><li>Apeldoorn</li><li>Arnhem</li><li>Beilen</li><li>Bergen Op Zoom</li><li>Bilthoven</li></ul>
  <ul class="city-list col-2"><li>Bussum</li><li>Dordrecht</li><li>Eindhoven</li><li>Enschede</li><li>Haarlem</li><li>Hilversum</li><li>Hoofddorp</li><li>Leiden</li><li>Leimuiden</li></ul>
  <ul class="city-list col-3"><li>Maastricht</li><li>Middleburg</li><li>Nieuwegein</li><li>Nijmegen</li><li>Roosendaal</li><li>Rotterdam</li><li>Schiphol</li><li>Sittard</li><li>Soest</li></ul>
  <ul class="city-list col-4"><li>The Hague</li><li>Tiel</li><li>Utrecht</li><li>Wassenaar</li><li>Zwolle</li></ul>

  <div class="region-map" role="img" aria-label="Clickable map of the Netherlands provinces with Drenthe highlighted in gold"></div>
  <div class="map-tag">Drenthe</div>

  <div class="info-panel"></div>
  <svg class="info-wedge" width="234" height="140" viewBox="0 0 234 140"><polygon points="0,0 234,140 0,140" fill="#f0f0f1"/></svg>
  <h2 class="info-title">Free Legal Information on Kwelderhofpunt</h2>
  <p class="info-lead">Can Help you make an educated decision when hiring an attorney</p>

  <div class="feature feat-qa">
    <svg width="74" height="74" viewBox="0 0 74 74"><circle cx="37" cy="37" r="35" fill="none" stroke="#e3a01b" stroke-width="2"/><ellipse cx="30" cy="32" rx="13" ry="8" fill="#e3a01b"/><polygon points="24,38 20,46 31,39" fill="#e3a01b"/><ellipse cx="45" cy="38" rx="13" ry="8" fill="#e3a01b" stroke="#f0f0f1" stroke-width="2"/><polygon points="50,44 54,51 43,45" fill="#e3a01b"/></svg>
    <div class="feature-label">Question &amp; Answers</div>
  </div>
  <div class="feature feat-centers">
    <svg width="74" height="74" viewBox="0 0 74 74"><circle cx="37" cy="37" r="35" fill="none" stroke="#e3a01b" stroke-width="2"/><g transform="rotate(-40 34 30)"><rect x="24" y="20" width="20" height="10" fill="#e3a01b"/><rect x="32" y="29" width="4" height="18" fill="#e3a01b"/></g><rect x="22" y="47" width="30" height="4" fill="#e3a01b"/><rect x="18" y="53" width="38" height="4" fill="#e3a01b"/></svg>
    <div class="feature-label">Legal Practice Centers</div>
  </div>
  <div class="feature feat-codes">
    <svg width="74" height="74" viewBox="0 0 74 74"><circle cx="37" cy="37" r="35" fill="none" stroke="#e3a01b" stroke-width="2"/><rect x="25" y="17" width="24" height="32" fill="none" stroke="#e3a01b" stroke-width="2.5"/><line x1="30" y1="25" x2="44" y2="25" stroke="#e3a01b" stroke-width="2"/><line x1="30" y1="31" x2="44" y2="31" stroke="#e3a01b" stroke-width="2"/><line x1="30" y1="37" x2="40" y2="37" stroke="#e3a01b" stroke-width="2"/><path d="M40 58 L40 44 Q40 41 43 41 Q46 41 46 44 L46 47 L52 48 Q55 49 54 53 L52 58 Z" fill="#e3a01b"/></svg>
    <div class="feature-label">Codes, Regulation &amp; Case Law</div>
  </div>

  <div class="footer-gold"></div>
  <footer class="site-footer">
    <div class="footer-links">Company<span>|</span>Terms of Service<span>|</span>Privacy Policy<span>|</span>Contact Us</div>
    <div class="copyright">Copyright kwelderhofpunt.com All Right Reserved.</div>
  </footer>
</body>
</html>
```